Flyer für Immobilienfirma
Zielgruppe
Immobilienfirma, klassisches Maklerunternehmen, Zielgruppe in erster Linie Familien.
Aufgabenstellung
Wir benötigen eine klassische Weihnachtskarte für unsere Kunden. Sehr schön wäre es, wenn unser Logo (als Datei anbei) mit auf der Karte erscheint. Es ist eine kreative, moderne, graphische Umsetzung des Themas 'Frohe Weihnachten' erwünscht, bitte eine Fotolösungen mit Weihnachtsbildern. Die Rückseite sollte inhaltlich wie im Beispiel gestaltet sein, die Schrift bitte aber passend zum Design der Vorderseite wählen. Wichtig, da die Karte am Ende über die Druckerei adresstechnisch personalisiert wird, benötigen wir am Ende noch die Schriftart.

```html
<!DOCTYPE html>
<html lang="de">
<head>
<meta charset="utf-8">
<title>Weihnachtskarte Lindquist Immobilien</title>
<link href="https://fonts.googleapis.com/css2?family=Teko:wght@600&family=Roboto:ital,wght@0,300;0,400;0,500;1,400&display=swap" rel="stylesheet">
<style>
  :root {
    --page: #f6f6f6;
    --red-dark: #d81f2a;
    --red: #ee2e3a;
    --red-light: #f5404b;
    --maroon: #9b1a22;
    --white: #ffffff;
    --ink: #2a2a2a;
  }
  * { margin: 0; padding: 0; box-sizing: border-box; }
  html, body { width: 1200px; height: 800px; overflow: hidden; background: var(--page); }
  body { position: relative; font-family: "Roboto", sans-serif; }

  .card {
    position: absolute;
    top: 150px;
    width: 350px;
    height: 495px;
    overflow: hidden;
    background: linear-gradient(160deg, var(--red-dark) 0%, var(--red) 55%, var(--red-light) 100%);
    box-shadow: 0 14px 30px rgba(0,0,0,.18);
  }
  .card--front { left: 215px; }
  .card--back  { left: 635px; }

  .card__footer {
    position: absolute; left: 0; bottom: 0;
    width: 350px; height: 110px;
    overflow: visible;
  }

  /* Front */
  .headline {
    position: absolute; left: 26px; top: 42px;
    font-family: "Teko", sans-serif; font-weight: 600;
    color: var(--white); text-transform: uppercase;
    line-height: .8; letter-spacing: 1px;
  }
  .headline span { display: block; }
  .headline .line-1 { font-size: 64px; }
  .headline .line-2 { font-size: 54px; margin-left: 12px; }
  .village {
    position: absolute; left: 80px; top: 195px;
    width: 200px; height: 165px;
    background: linear-gradient(180deg, #f3f3f3 0%, #e9d2d4 45%, var(--maroon) 100%);
    border-radius: 6px;
  }

  /* Back */
  .letter {
    position: absolute; left: 30px; right: 30px; top: 56px;
    color: var(--white); text-align: center;
  }
  .letter__greeting { font-style: italic; font-size: 15px; line-height: 1.3; margin-bottom: 14px; }
  .letter__text { font-weight: 300; font-size: 10.5px; line-height: 1.45; margin-bottom: 10px; }
  .letter__closing { font-weight: 300; font-size: 10.5px; margin-top: 16px; }
  .signature {
    width: 120px; height: 44px; margin: 8px auto 0;
    background: linear-gradient(90deg, rgba(255,255,255,.15), rgba(255,255,255,.32), rgba(255,255,255,.15));
    border-radius: 4px;
  }

  .brand {
    position: absolute; display: flex; align-items: center; gap: 6px;
    font-family: "Roboto", sans-serif; font-weight: 500; font-size: 13px; color: var(--ink);
    white-space: nowrap;
  }
  .brand__dot { width: 10px; height: 10px; border-radius: 50%; background: var(--red); }
  .card--front .brand { left: 50%; transform: translateX(-50%); bottom: 30px; }
  .card--back .brand { right: 18px; bottom: 22px; }

  .contact {
    position: absolute; left: 20px; bottom: 14px;
    font-size: 9px; line-height: 1.5; color: var(--ink);
  }
  .contact__name { color: var(--red); font-weight: 500; }
  .contact__label { color: var(--red); }
</style>
</head>
<body>

  <article class="card card--front">
    <h1 class="headline"><span class="line-1">Frohe</span><span class="line-2">Weihnachten</span></h1>
    <div class="village" role="img" aria-label="Illustration eines verschneiten Dorfes mit Häusern und Tannen"></div>
    <svg class="card__footer" viewBox="0 0 350 110" aria-hidden="true">
      <path d="M0 110 L0 36 L140 36 L175 8 L210 36 L350 36 L350 110 Z" fill="var(--white)"/>
      <path d="M0 28 L137 28 L175 -2 L213 28 L350 28" fill="none" stroke="var(--red)" stroke-width="3"/>
    </svg>
    <div class="brand"><span class="brand__dot"></span>Lindquist Immobilien</div>
  </article>

  <article class="card card--back">
    <div class="letter">
      <p class="letter__greeting">Liebe Kunden,<br>Geschäftspartner und Freunde!</p>
      <p class="letter__text">Wir möchten uns für Ihr entgegengebrachtes Vertrauen und die angenehme Zusammenarbeit bedanken.</p>
      <p class="letter__text">Genießen Sie die Weihnachtszeit mit vielen kleinen Freuden und kommen Sie gesund ins Jahr 2025.</p>
      <p class="letter__text">Aufgrund der aktuellen Notlage vieler Menschen möchten wir in diesem Jahr erneut mit einer Spende an den Kinderfonds der Stadt Kelbach versuchen, ein wenig Freude und Zuversicht zu schenken.</p>
      <p class="letter__closing">Ihr Immobilienteam von</p>
      <div class="signature" role="img" aria-label="Handschriftliche Unterschrift des Teams"></div>
    </div>
    <svg class="card__footer" viewBox="0 0 350 110" aria-hidden="true">
      <path d="M0 110 L0 40 L235 40 L270 10 L305 40 L350 40 L350 110 Z" fill="var(--white)"/>
      <path d="M0 32 L232 32 L270 0 L308 32 L350 32" fill="none" stroke="var(--red)" stroke-width="3"/>
    </svg>
    <div class="contact">
      <p class="contact__name">Lindquist Immobilien</p>
      <p>Brunnenweg 12 | 90000 Kelbach</p>
      <p><span class="contact__label">Tel.:</span> 01234 567890</p>
      <p>www.lindquist-immobilien.de</p>
    </div>
    <div class="brand"><span class="brand__dot"></span>Lindquist Immobilien</div>
  </article>

</body>
</html>
```